the look of import selling star-up company

I have attached rhino logo that i like (can be edit) and i wanna turn that in to luxury look. Example like black base and gold logo +luxury looking font.

Company name: Brevan trading Oy
Slogan: Ordinary is not an option.
CEO Juho Kettumaa
Starting to import ceramic nano coatings to cars, in home use and industrial purposes.

Target Market(s)

30-60 year old men and women ho have big money and know what car they drive

Industry/Entity Type

It Company

```html
<!DOCTYPE html>
<html lang="en">
<head>
<meta charset="utf-8">
<title>Brevan trading Oy – Business Card</title>
<link href="https://fonts.googleapis.com/css2?family=Roboto:wght@300;400&family=Saira+Semi+Condensed:wght@600;700&display=swap" rel="stylesheet">
<style>
  :root {
    --backdrop: #8e8f8f;
    --card: #1b1b1b;
    --gold: #d6ad2c;
    --text: #e6e6e6;
    --text-soft: #b5b5b5;
  }
  * { margin: 0; padding: 0; box-sizing: border-box; }
  html, body {
    width: 1200px; height: 781px; overflow: hidden;
    background: var(--backdrop);
  }
  .canvas { position: relative; width: 1200px; height: 781px; }

  .card {
    position: absolute;
    left: 358px;
    width: 452px; height: 251px;
    background: var(--card);
  }
  .card--front { top: 103px; }
  .card--back  { top: 410px; }

  .brand {
    position: absolute;
    display: flex; flex-direction: column; align-items: center;
    color: var(--gold);
    text-align: center;
  }
  .brand__ring {
    border: 3px solid var(--gold);
    border-radius: 50%;
  }
  .brand__name {
    font-family: "Saira Semi Condensed", sans-serif;
    font-weight: 700;
    text-transform: uppercase;
    color: var(--gold);
  }
  .brand__slogan {
    font-family: "Roboto", sans-serif;
    font-weight: 300;
    font-size: 10px;
    letter-spacing: 3px;
    text-transform: uppercase;
    color: var(--text-soft);
  }

  .card--front .brand {
    left: 0; right: 0; top: 50%; transform: translateY(-50%);
  }
  .card--front .brand__ring { width: 56px; height: 56px; margin-bottom: 16px; }
  .card--front .brand__name { font-size: 24px; letter-spacing: 5px; line-height: 28px; }
  .card--front .brand__slogan { margin-top: 10px; }

  .card--back .brand {
    left: 30px; width: 180px; top: 50%; transform: translateY(-50%);
  }
  .card--back .brand__ring { width: 48px; height: 48px; margin-bottom: 14px; }
  .card--back .brand__name { font-size: 18px; letter-spacing: 3px; line-height: 22px; }

  .contact {
    position: absolute; left: 244px; top: 56px;
    font-family: "Roboto", sans-serif; color: var(--text);
  }
  .contact__name {
    font-family: "Saira Semi Condensed", sans-serif;
    font-weight: 700; font-size: 20px; line-height: 22px; color: #f2f2f2;
    letter-spacing: 0.3px;
  }
  .contact__role { font-size: 10px; line-height: 12px; color: var(--text-soft); margin-top: 1px; }
  .contact__address { font-size: 11.5px; line-height: 15px; margin-top: 23px; }
  .contact__list { list-style: none; margin-top: 6px; }
  .contact__item {
    display: flex; align-items: center; gap: 8px;
    font-size: 11.5px; line-height: 15px;
  }
  .contact__icon { width: 11px; height: 11px; fill: var(--text-soft); flex: none; }
</style>
</head>
<body>
<main class="canvas">

  <section class="card card--front" aria-label="Card front">
    <div class="brand">
      <span class="brand__ring"></span>
      <span class="brand__name">Brevan trading Oy</span>
      <span class="brand__slogan">Ordinary is not an option.</span>
    </div>
  </section>

  <section class="card card--back" aria-label="Card back">
    <div class="brand">
      <span class="brand__ring"></span>
      <span class="brand__name">Brevan<br>trading Oy</span>
    </div>

    <div class="contact">
      <h1 class="contact__name">Juho Kettumaa</h1>
      <p class="contact__role">CEO</p>
      <p class="contact__address">48 Harbor Lane<br>Eastfield City 20417</p>
      <ul class="contact__list">
        <li class="contact__item">
          <svg class="contact__icon" viewBox="0 0 12 12" aria-hidden="true"><path d="M1 4c0-2 2-3 5-3s5 1 5 3v1H8.5V3.6c-1.6-.5-3.4-.5-5 0V5H1z"/><rect x="2" y="6" width="8" height="5" rx="1"/></svg>
          <span>000-222-3333</span>
        </li>
        <li class="contact__item">
          <svg class="contact__icon" viewBox="0 0 12 12" aria-hidden="true"><path d="M0 2h12v1L6 7 0 3z"/><path d="M0 4.2l6 4 6-4V10H0z"/></svg>
          <span>j.kettumaa@brevantradingoy.com</span>
        </li>
        <li class="contact__item">
          <svg class="contact__icon" viewBox="0 0 12 12" aria-hidden="true"><path d="M6 0a6 6 0 1 0 0 12A6 6 0 0 0 6 0zm4.8 5.3H8.6a9 9 0 0 0-1-3.9 4.9 4.9 0 0 1 3.2 3.9zM6 1.2c.7.8 1.3 2.3 1.4 4.1H4.6C4.7 3.5 5.3 2 6 1.2zM4.4 1.4a9 9 0 0 0-1 3.9H1.2a4.9 4.9 0 0 1 3.2-3.9zM1.2 6.7h2.2a9 9 0 0 0 1 3.9 4.9 4.9 0 0 1-3.2-3.9zM6 10.8c-.7-.8-1.3-2.3-1.4-4.1h2.8c-.1 1.8-.7 3.3-1.4 4.1zm1.6-.2a9 9 0 0 0 1-3.9h2.2a4.9 4.9 0 0 1-3.2 3.9z"/></svg>
          <span>www.brevantradingoy.com</span>
        </li>
      </ul>
    </div>
  </section>

</main>
</body>
</html>
```